Vietnamese Restaurant Poster

We are a family restaurant specializing in Vietnamese comfort food of pho (Vietnamese Beef Noodle Soup).

We need to create a poster that will attract customers driving by our restaurant.

This poster will be placed on sandwich boards and placed on the intersecting streets.

We want it to be
- big and visually appealing.
- Preferably with a logo incorporating our name and a bowl of Pho
- a arrow sign pointing right
- our phone number 604-318-7915

The name of our restaurant is:

Pho Lanh Tuyet (Title text)
Vietnamese Restaurant (smaller text)

Reason: We have narrowed it down to 2  designs that we absolutely love. Thank you to all who have submitted.

Target Market(s)

Caucasian people who have not tried Vietnamese food. Our location is a little hidden so we want to make these posters to put on the main streets which will grab attention of people driving by to come into our restaurant

Industry/Entity Type

Restaurant

Requirements
Must have
• - big and visually appealing.
logo incorporating our name and a bowl of Pho
Nice to have
• a person eating a bowl of pho

```html
<!DOCTYPE html>
<html lang="en">
<head>
<meta charset="utf-8">
<title>Pho Lanh Tuyet – Vietnamese Restaurant</title>
<link rel="stylesheet" href="https://fonts.googleapis.com/css2?family=Tinos:ital,wght@0,400;0,700;1,400;1,700&display=swap">
<style>
  :root {
    --sun-light: #fdf1a6;
    --sun-mid: #fcd84a;
    --sun-edge: #f4b400;
    --brand-red: #c41c24;
    --ink: #111111;
    --paper: #ffffff;
    --figure-light: #d9a45c;
    --figure-dark: #8a5a2b;
  }
  html, body {
    margin: 0;
    padding: 0;
    overflow: hidden;
    background: var(--paper);
  }
  .poster {
    position: relative;
    width: 900px;
    height: 1200px;
    overflow: hidden;
    background: radial-gradient(ellipse 620px 760px at 450px 600px, var(--sun-light) 0%, var(--sun-mid) 45%, var(--sun-edge) 100%);
    font-family: "Tinos", "Times New Roman", serif;
  }
  .poster__title {
    position: absolute;
    left: 0;
    top: 42px;
    width: 900px;
    margin: 0;
    text-align: center;
    font-style: italic;
    font-weight: 400;
    font-size: 122px;
    line-height: 1;
    color: var(--brand-red);
    letter-spacing: -1px;
  }
  .poster__diner {
    position: absolute;
    left: 210px;
    top: 180px;
    width: 500px;
    height: 520px;
    border-radius: 46% 46% 30% 30%;
    background: radial-gradient(ellipse at 50% 45%, var(--figure-light) 0%, var(--figure-dark) 100%);
    opacity: 0.85;
  }
  .poster__arrow {
    position: absolute;
    left: 0;
    top: 700px;
    width: 900px;
    height: 240px;
  }
  .poster__arrow-shape {
    fill: var(--brand-red);
  }
  .poster__subtitle {
    position: absolute;
    left: 78px;
    top: 768px;
    margin: 0;
    font-style: italic;
    font-weight: 400;
    font-size: 76px;
    line-height: 1.2;
    color: var(--paper);
    white-space: nowrap;
  }
  .poster__phone-label {
    position: absolute;
    left: 24px;
    top: 970px;
    margin: 0;
    font-weight: 700;
    font-size: 64px;
    line-height: 1;
    color: var(--ink);
  }
  .poster__phone-band {
    position: absolute;
    left: 0;
    bottom: 0;
    width: 900px;
    height: 138px;
    background: var(--ink);
    display: flex;
    align-items: center;
    justify-content: center;
  }
  .poster__phone-number {
    margin: 0;
    font-weight: 700;
    font-size: 134px;
    line-height: 1;
    color: var(--paper);
    letter-spacing: 1px;
  }
</style>
</head>
<body>
  <main class="poster">
    <h1 class="poster__title">Pho Lanh Tuyet</h1>

    <div class="poster__diner" role="img" aria-label="Illustration of a man in glasses and a brown jacket eating a red bowl of pho with a spoon"></div>

    <svg class="poster__arrow" viewBox="0 0 900 240" aria-hidden="true">
      <path class="poster__arrow-shape" d="M70 56 H690 V4 L874 120 L690 236 V186 H70 Q36 186 36 152 V90 Q36 56 70 56 Z"/>
    </svg>
    <p class="poster__subtitle">Vietnamese Restaurant</p>

    <p class="poster__phone-label">our phone number:</p>
    <div class="poster__phone-band">
      <p class="poster__phone-number">604-318-7915</p>
    </div>
  </main>
</body>
</html>
```